IT Company Business Card Rebranding

We want to modernize our business cards massively. We want to incorporate aspects of our old business card such as the white and geometric design with the blues of another icon. Existing Logo, old business card and icon are all attached.

We are a modern IT company that provides support for new and growing technologies and want our business cards to be modern yet professional.
Updates

Industry/Entity Type

Information Technology

Contact Information for Business Card

Roughly 43 : 26 or 1075 x 650 px

Font styles to use
Serif

Colors
0492cd
3276b5
33a6d7
86cfc6
cfeae6
cee9f5
ffffff

Requirements
Must have
• Modern yet professional
Nice to have
• We would like to incorporate the blues of our existing logo and of the icon provided. Really like the design of the icon.
Should not have
• Too Decorative. Just simple and professional.
• Not have the circle icon, as it is a copyrighted icon, I just like the colors and the geometric design

```html
<!DOCTYPE html>
<html lang="en">
<head>
<meta charset="utf-8">
<title>Nexora Tech — Business Card</title>
<link rel="stylesheet" href="https://fonts.googleapis.com/css2?family=Open+Sans:wght@400;600;700&display=swap">
<style>
  :root {
    --backdrop: #e8e9eb;
    --paper: #f7f8f9;
    --royal: #1d5fc4;
    --blue: #3276b5;
    --sky: #0492cd;
    --teal: #14a3ad;
    --ink-grey: #6a6e74;
    --white: #ffffff;
  }
  * { box-sizing: border-box; margin: 0; padding: 0; }
  html, body {
    width: 1200px; height: 800px; overflow: hidden;
    background: var(--backdrop);
    font-family: "Open Sans", Arial, sans-serif;
  }
  .sheet {
    width: 1200px; height: 800px;
    display: flex; align-items: center; justify-content: center; gap: 40px;
  }
  .card {
    position: relative;
    width: 520px; height: 314px;
    background: var(--paper);
    overflow: hidden;
    box-shadow: 0 6px 18px rgba(0,0,0,.12);
  }

  /* Soft gradient fields standing in for the geometric artwork */
  .artwork {
    position: absolute;
  }
  .artwork--top {
    left: 0; right: 0; top: 0; height: 120px;
    background: linear-gradient(90deg, var(--teal), var(--sky) 50%, var(--royal));
    clip-path: polygon(0 0, 100% 0, 100% 22%, 0 100%);
  }
  .artwork--bottom {
    left: 0; right: 0; bottom: 0; height: 136px;
    background: linear-gradient(90deg, var(--royal), var(--sky) 55%, var(--teal));
    clip-path: polygon(0 50%, 100% 0, 100% 100%, 0 100%);
  }
  .artwork--panel {
    top: 0; bottom: 0; right: 0; width: 306px;
    background: linear-gradient(160deg, var(--sky), var(--blue) 60%, var(--royal));
    clip-path: polygon(0 0, 100% 0, 100% 100%, 20% 100%);
  }

  /* Front: brand side */
  .brand {
    position: absolute; left: 0; right: 0; top: 132px;
    display: flex; align-items: center; justify-content: center; gap: 16px;
  }
  .brand__dot {
    width: 22px; height: 22px; border-radius: 50%;
    background: var(--royal);
  }
  .brand__name {
    font-size: 30px; font-weight: 400; letter-spacing: .3em;
    color: var(--ink-grey); text-transform: uppercase;
  }

  /* Back: contact side */
  .brand--small { top: auto; bottom: 72px; left: 0; right: auto; width: 250px; gap: 10px; }
  .brand--small .brand__dot { width: 14px; height: 14px; }
  .brand--small .brand__name { font-size: 15px; letter-spacing: .25em; }

  .contact {
    position: absolute; left: 322px; top: 52px;
    color: var(--white);
  }
  .contact__name { font-size: 30px; font-weight: 700; line-height: 1; letter-spacing: .02em; }
  .contact__role { font-size: 14px; font-weight: 600; letter-spacing: .06em; margin-top: 4px; }
  .contact__rule { width: 150px; height: 1px; background: var(--white); margin: 10px 0 16px; }
  .contact__list { list-style: none; }
  .contact__item {
    display: flex; align-items: center; gap: 10px;
    font-size: 14px; margin-bottom: 11px;
  }
  .contact__icon {
    width: 20px; height: 20px; border-radius: 50%;
    background: var(--white);
    display: flex; align-items: center; justify-content: center;
    flex: none;
  }
  .contact__icon svg { width: 12px; height: 12px; }
</style>
</head>
<body>
<main class="sheet">

  <!-- Front -->
  <section class="card card--front" aria-label="Card front">
    <div class="artwork artwork--top" role="img" aria-label="Blue and teal geometric pattern"></div>
    <div class="artwork artwork--bottom" role="img" aria-label="Blue and teal geometric pattern"></div>
    <div class="brand">
      <span class="brand__dot"></span>
      <span class="brand__name">Nexora Tech</span>
    </div>
  </section>

  <!-- Back -->
  <section class="card card--back" aria-label="Card back">
    <div class="artwork artwork--panel" role="img" aria-label="Blue geometric pattern"></div>

    <div class="brand brand--small">
      <span class="brand__dot"></span>
      <span class="brand__name">Nexora Tech</span>
    </div>

    <div class="contact">
      <p class="contact__name">MARCUS</p>
      <p class="contact__role">TECHNICAL SERVICES</p>
      <div class="contact__rule"></div>
      <ul class="contact__list">
        <li class="contact__item">
          <span class="contact__icon">
            <svg viewBox="0 0 24 24"><path fill="#1d5fc4" d="M6.6 10.8a15 15 0 0 0 6.6 6.6l2.2-2.2c.3-.3.7-.4 1-.2 1.1.4 2.3.6 3.6.6.6 0 1 .4 1 1V20c0 .6-.4 1-1 1A17 17 0 0 1 3 4c0-.6.4-1 1-1h3.5c.6 0 1 .4 1 1 0 1.3.2 2.5.6 3.6.1.3 0 .7-.2 1z"/></svg>
          </span>
          xxxxxxxxxxx
        </li>
        <li class="contact__item">
          <span class="contact__icon">
            <svg viewBox="0 0 24 24"><rect x="2" y="5" width="20" height="14" rx="2" fill="#1d5fc4"/><path d="M3 6l9 7 9-7" fill="none" stroke="#fff" stroke-width="2"/></svg>
          </span>
          hello@nexoratech.com
        </li>
        <li class="contact__item">
          <span class="contact__icon">
            <svg viewBox="0 0 24 24" fill="none" stroke="#1d5fc4" stroke-width="2"><circle cx="12" cy="12" r="9"/><path d="M3 12h18M12 3c3 3 3 15 0 18M12 3c-3 3-3 15 0 18"/></svg>
          </span>
          www.nexoratech.com
        </li>
      </ul>
    </div>
  </section>

</main>
</body>
</html>
```